Marcus Bellamy & Golden Lanterns

I need a cd cover designed for a Gospel/Christian Choir. I'm attaching the main picture I want on the cover. This is our single "Hold on through morning".

Requirements
Must have
• Single name: Hold On Through Morning

```html
<!DOCTYPE html>
<html lang="en">
<head>
<meta charset="utf-8">
<title>Marcus Bellamy &amp; Golden Lanterns – Hold On Through Morning</title>
<link href="https://fonts.googleapis.com/css2?family=Cinzel:wght@400;600;700&display=swap" rel="stylesheet">
<style>
  :root {
    --page-bg: #ffffff;
    --frame: #000000;
    --ember: #e0531c;
    --amber: #f39a2a;
    --deep-red: #8a1e12;
    --night: #0d0c16;
    --suit-blue: #23214a;
    --suit-deep: #0f0e22;
    --band: rgba(10, 10, 20, 0.55);
    --band-light: rgba(40, 40, 55, 0.35);
    --silver: #e9e9ee;
    --silver-dark: #9c9ca8;
  }
  * { margin: 0; padding: 0; box-sizing: border-box; }
  html, body {
    width: 1200px; height: 1000px; overflow: hidden;
    background: var(--page-bg);
  }
  .cover-frame {
    position: absolute; left: 131px; top: 31px;
    width: 938px; height: 938px;
    background: var(--frame);
  }
  .cover {
    position: absolute; left: 20px; top: 20px;
    width: 898px; height: 898px; overflow: hidden;
  }
  .cover-backdrop {
    position: absolute; inset: 0;
    background:
      radial-gradient(ellipse 260px 200px at 100px 40px, rgba(243,110,30,0.85), transparent 70%),
      radial-gradient(ellipse 380px 300px at 700px 150px, rgba(243,154,42,0.9), transparent 70%),
      radial-gradient(ellipse 300px 260px at 820px 60px, rgba(224,83,28,0.9), transparent 70%),
      radial-gradient(ellipse 120px 160px at 40px 460px, rgba(243,154,42,0.55), transparent 70%),
      linear-gradient(180deg, var(--deep-red) 0%, #3a1a18 35%, var(--night) 70%, #08070d 100%);
  }
  .portrait {
    position: absolute; left: 10px; top: 55px;
    width: 840px; height: 843px;
    border-radius: 46% 46% 0 0 / 30% 30% 0 0;
    background:
      radial-gradient(ellipse 140px 170px at 440px 170px, rgba(92,58,44,0.95), rgba(60,36,30,0.7) 60%, transparent 100%),
      radial-gradient(ellipse 380px 480px at 560px 620px, var(--suit-blue), var(--suit-deep) 75%, transparent 100%),
      linear-gradient(180deg, rgba(40,24,30,0.35) 0%, rgba(20,18,40,0.7) 60%, rgba(10,10,22,0.85) 100%);
  }
  .title-band {
    position: absolute; left: 0; right: 0; top: 494px; height: 163px;
    background: var(--band);
  }
  .subtitle-band {
    position: absolute; left: 0; right: 0; top: 657px; height: 61px;
    background: var(--band-light);
  }
  .artist, .ensemble, .single {
    position: absolute; left: 0; right: 0; text-align: center;
    font-family: "Cinzel", "Trajan Pro", serif;
    line-height: 1;
    white-space: nowrap;
    color: var(--silver);
    background: linear-gradient(180deg, #ffffff 0%, var(--silver) 45%, var(--silver-dark) 60%, #f4f4f8 100%);
    -webkit-background-clip: text; background-clip: text;
    -webkit-text-fill-color: transparent;
    filter: drop-shadow(0 2px 2px rgba(0,0,0,0.7));
  }
  .artist { top: 502px; font-size: 80px; font-weight: 600; letter-spacing: 2px; }
  .ensemble { top: 590px; font-size: 52px; font-weight: 600; letter-spacing: 1px; }
  .single-row {
    position: absolute; left: 0; right: 0; top: 672px; height: 32px;
  }
  .single { top: 0; font-size: 27px; font-weight: 700; letter-spacing: 1px; }
  .rule { position: absolute; top: 14px; }
  .rule-left { left: 94px; }
  .rule-right { right: 80px; }
  .cross-mark {
    position: absolute; left: 420px; top: 716px;
  }
</style>
</head>
<body>
  <div class="cover-frame">
    <div class="cover">
      <div class="cover-backdrop"></div>
      <div class="portrait" role="img" aria-label="Photo of the lead singer in a dark satin suit and patterned tie, seated before a warm orange and red glowing background"></div>
      <div class="title-band"></div>
      <div class="subtitle-band"></div>
      <h1 class="artist">Marcus Bellamy</h1>
      <h2 class="ensemble">&amp; Golden Lanterns</h2>
      <div class="single-row">
        <svg class="rule rule-left" width="126" height="6" viewBox="0 0 126 6" aria-hidden="true">
          <polygon points="0,3 110,1 126,3 110,5" fill="#e9e9ee"/>
        </svg>
        <p class="single">Hold On Through Morning</p>
        <svg class="rule rule-right" width="126" height="6" viewBox="0 0 126 6" aria-hidden="true">
          <polygon points="126,3 16,1 0,3 16,5" fill="#e9e9ee"/>
        </svg>
      </div>
      <svg class="cross-mark" width="56" height="102" viewBox="0 0 56 102" aria-hidden="true">
        <polygon points="28,0 31,30 56,36 31,41 28,102 25,41 0,36 25,30" fill="#e9e9ee"/>
        <polygon points="28,28 33,36 28,44 23,36" fill="#8e8e9a"/>
      </svg>
    </div>
  </div>
</body>
</html>
```